Full Truck Wrap for residential and commercial roofing company

I am looking to get my trucks wrapped to help build brand in newer markets that aren't growing as fast as we would like due to branding not popping out as much as we like! We are a roofing company who provides roofing services to residential and commercial property owners in Alabama & Georgia in the united states. Our main services are storm restoration, roofing, gutters, siding, assisting clients in insurance claims to restore their properties after a loss due to severe storms.

My goal with this truck wrap is to generate a truck wrap we can use for the next 5-10 years on several different types of vehicles and job trailers. I would like to keep the design simple yet, professional, modern, easy to read, and rememberable. We want to have the rear window wrapped as well to provide information to people sitting behind us in traffic or sees our vehicles parked somewhere. Information on rear window needs to have Sales Rep first and last name, phone number, company website, and etc.

I will attach a few example of wraps that I liked and thought looked good to me and was something we could easily use for years to come. Please submit any ideas you have for review as i am open to any recommendations for this wrap, providing this information as a starting point. Attached are 2 different logos we have, don't want both logos on same design only providing them both incase a design looks better with the other. I also added some side shots of the trucks needing wraps incase you are able to provided a proof with that so we can see it on the first truck getting wrapped.
Updates

still looking for a design for this contest, nothing has really been what i was expecting. please upload more if you have more design recommendations

Target Market(s)

Higher in residential properties and business owners with properties

Industry/Entity Type

Roofing Company, residential and commercial construction

Font styles to use
Sans Serif

Requirements
Nice to have
• Modern design that is more of a corporation look. We will be wrapping our entire fleet with this new wrap design.
Should not have
• Similar designs to generic wrap designs

```html
<!DOCTYPE html>
<html lang="en">
<head>
<meta charset="utf-8">
<title>Summit Crest Roofing – Fleet Wrap Concepts</title>
<link href="https://fonts.googleapis.com/css2?family=Montserrat:wght@700;800&family=Oswald:wght@500;600&display=swap" rel="stylesheet">
<style>
  :root {
    --wrap-red: #c8141b;
    --wrap-black: #0d0d0d;
    --wrap-white: #ffffff;
    --canvas-bg: #f1f1f1;
    --ghost: #1c1c1c;
  }
  html, body {
    margin: 0;
    padding: 0;
    width: 1200px;
    height: 1200px;
    overflow: hidden;
    background: var(--canvas-bg);
  }
  .sheet {
    width: 1200px;
    height: 1200px;
    display: flex;
    flex-direction: column;
    justify-content: center;
    align-items: center;
    gap: 120px;
  }
  .wrap-panel {
    width: 1100px;
    height: 320px;
    display: block;
    box-shadow: 0 6px 18px rgba(0,0,0,0.12);
  }
  .brand-name { font-family: 'Montserrat', sans-serif; font-weight: 800; fill: var(--wrap-red); letter-spacing: 1px; }
  .service-line { font-family: 'Oswald', sans-serif; font-weight: 600; letter-spacing: 0.5px; }
  .phone-line { font-family: 'Oswald', sans-serif; font-weight: 500; }
  .web-line { font-family: 'Montserrat', sans-serif; font-weight: 700; letter-spacing: 2px; }
  .ghost-name { font-family: 'Montserrat', sans-serif; font-weight: 800; fill: var(--ghost); }
</style>
</head>
<body>
<main class="sheet">

  <!-- Concept A: white body, black swoosh, red bed -->
  <svg class="wrap-panel wrap-panel--white" viewBox="0 0 1100 320" xmlns="http://www.w3.org/2000/svg" aria-label="Wrap concept A, side view">
    <rect class="panel-base" x="0" y="0" width="1100" height="320" fill="var(--wrap-white)"/>
    <path class="black-swoosh" d="M150 230 L540 230 C600 230 620 110 680 104 L1100 96 L1100 140 L700 148 C650 152 630 276 560 276 L150 276 Z" fill="var(--wrap-black)"/>
    <path class="red-bed" d="M150 282 L570 282 C640 276 664 156 712 152 L1100 144 L1100 300 L560 300 L560 288 L150 288 Z" fill="var(--wrap-red)"/>

    <rect class="logo-square" x="150" y="128" width="36" height="36" fill="var(--wrap-red)"/>
    <text class="brand-name" x="200" y="160" font-size="34">SUMMIT CREST</text>
    <text class="brand-name" x="200" y="190" font-size="22">ROOFING</text>

    <text class="web-line" x="190" y="260" font-size="20" fill="var(--wrap-white)">www.summitcrestga.com</text>

    <text class="service-line" x="700" y="88" font-size="16" fill="var(--wrap-black)">STORM RESTORATION | ROOFING | GUTTERS | SIDING</text>
    <text class="phone-line" x="790" y="132" font-size="28" letter-spacing="4" fill="var(--wrap-white)">555-014-2290</text>
  </svg>

  <!-- Concept B: black body, red accents -->
  <svg class="wrap-panel wrap-panel--black" viewBox="0 0 1100 320" xmlns="http://www.w3.org/2000/svg" aria-label="Wrap concept B, side view">
    <rect class="panel-base" x="0" y="0" width="1100" height="320" fill="var(--wrap-white)"/>
    <path class="black-body" d="M240 110 L1100 80 L1100 286 L240 286 Z" fill="var(--wrap-black)"/>
    <path class="red-front-slash" d="M120 170 L290 104 L340 104 L180 190 Z" fill="var(--wrap-red)"/>
    <path class="red-top-stripe" d="M290 98 L1100 66 L1100 78 L300 108 Z" fill="var(--wrap-red)"/>
    <rect class="red-bottom-band" x="240" y="266" width="860" height="14" fill="var(--wrap-red)"/>

    <text class="ghost-name" x="700" y="250" font-size="80">SUMMIT</text>

    <rect class="service-tag" x="640" y="56" width="400" height="30" fill="var(--wrap-red)"/>
    <text class="service-line" x="660" y="77" font-size="16" fill="var(--wrap-white)">STORM RESTORATION   ROOFING   GUTTERS   SIDING</text>

    <text class="web-line" x="620" y="126" font-size="16" fill="var(--wrap-white)">www.summitcrestga.com</text>
    <rect class="divider" x="896" y="106" width="3" height="26" fill="var(--wrap-white)"/>
    <text class="phone-line" x="912" y="128" font-size="24" letter-spacing="2" fill="var(--wrap-red)">555-014-2290</text>

    <rect class="logo-square" x="270" y="166" width="36" height="36" fill="var(--wrap-red)"/>
    <text class="brand-name" x="320" y="198" font-size="34">SUMMIT CREST</text>
    <text class="brand-name" x="320" y="228" font-size="22">ROOFING</text>
  </svg>

</main>
</body>
</html>
```